Velvet Orchard Website A Website design for book editing

A website design for book editing

Our proofreading, editing and manuscript review packages are specifically tailored to help you publish the best possible version of your story.

NEED HELP PUBLISHING A BESTSELLER?

If you’re looking for professional book editing services from senior publishing industry insiders, look no further. Besides editing, we can also answer all your publishing questions and get you started building your author platform.

OUR SERVICES

We've carefully structured our packages to maximize value for every budget.

PRICING

$.02
PER WORD
Proofreading
Line Edit (Copy-editing)
Fix spelling and grammar
Sales copy/summary revision

$.04
PER WORD
Proofreading
Line Edit (Copy-editing)
Fix spelling and grammar
Organization and content
Plot and pacing
Manuscript Review

$.06
PER WORD
Proofreading
Line Edit (Copy-editing)
Fix spelling and grammar
Organization and content
Plot and pacing
Manuscript Review
Formatting (print and ebook)
Pre-publication proofread

OUR PROCESS

Send us a sample of your book. Our caffeine-fueled, eagle-eyed editors will go through it and then email you with their comments and suggestions. You can ask them any questions you want. They will look for…

Typos and grammatical errors.
Spelling and word choice issues
Punctuation and style
Word choice, clarity and flow.
Sentence structure and craft
If your writing is already clean, then they’ll discuss bigger picture things with you, like theme, concept, purpose, audience, potential market and branding (including title, subtitle, and tagline or elevator pitch).

Once you feel comfortable and confident in an editor’s expertise, skill and knowledge, and are ready to move ahead, we’ll send an invoice for the first half of the total word count so the editor can get started. We’ll charge the rest when the project is close to completion.

Target Market(s)

Authors

Industry/Entity Type

Book Publisher

Coding

Coded - Design and coding required

Number of Pages Required

1 page

Requirements
Must have
• OUR SERVICES
• We've carefully structured our packages to maximize value for every budget.
• PRICING
• $.02
• PER WORD
• Proofreading
• Line Edit (Copy-editing)
• Fix spelling and grammar
• Sales copy/summary revision
• $.04
• PER WORD
• Proofreading
• Organization and content
• Plot and pacing
• Manuscript Review
• $.06
• PER WORD
• Proofreading
• Plot and pacing
• Manuscript Review
• Formatting (print and ebook)
• Pre-publication proofread

```html
<!DOCTYPE html>
<html lang="en">
<head>
<meta charset="utf-8">
<title>Velvet Orchard — Book Editing</title>
<link href="https://fonts.googleapis.com/css2?family=Lato:ital,wght@0,300;0,400;0,700;1,400&family=Open+Sans:ital,wght@0,400;0,600;1,400&display=swap" rel="stylesheet">
<style>
:root{
  --red:#d4101e;
  --ink:#222222;
  --text:#444444;
  --muted:#666666;
  --light:#ebebeb;
  --card-head:#d9d9d9;
  --dark:#2d2d2d;
  --white:#ffffff;
}
*{box-sizing:border-box;margin:0;padding:0}
html,body{width:1200px;height:3035px;overflow:hidden;background:var(--white)}
body{position:relative;font-family:"Open Sans",Arial,sans-serif;color:var(--text)}
.abs{position:absolute}

/* Header */
.site-header{position:absolute;left:0;top:0;width:1200px;height:101px;background:var(--white);z-index:5}
.brand{position:absolute;left:150px;top:40px;display:flex;align-items:center;gap:10px;font-family:"Lato",sans-serif;font-weight:700;font-size:34px;color:var(--red);line-height:1}
.brand-dot{width:14px;height:14px;border-radius:50%;background:var(--ink)}
.main-nav{position:absolute;left:470px;top:50px;display:flex;gap:34px;font-family:"Lato",sans-serif;font-weight:700;font-size:18px;color:var(--ink)}
.main-nav .active{color:var(--red)}

/* Hero */
.hero{position:absolute;left:0;top:101px;width:1200px;height:612px;
  background:linear-gradient(100deg,#8a5a4a 0%,#a88a78 30%,#b9aea3 55%,#8c8680 80%,#6f6a66 100%)}
.hero-shade{position:absolute;inset:0;background:rgba(40,40,40,.35)}
.hero-title{position:absolute;left:0;width:1200px;top:200px;text-align:center;font-family:"Lato",sans-serif;font-weight:400;font-size:46px;line-height:46px;color:var(--white);text-transform:uppercase;letter-spacing:.5px}
.btn-outline{position:absolute;left:516px;top:317px;width:160px;height:42px;border:2px solid var(--white);color:var(--white);font-family:"Lato",sans-serif;font-weight:700;font-size:15px;display:flex;align-items:center;justify-content:center}
.hero-dots{position:absolute;left:552px;top:540px;display:flex;gap:9px}
.hero-dots span{width:14px;height:14px;border-radius:50%;background:var(--white)}
.hero-dots span:first-child{background:transparent;border:2px solid var(--white)}

/* Section headings */
.section-title{font-family:"Lato",sans-serif;font-weight:400;font-size:38px;color:var(--ink);display:flex;align-items:flex-end;gap:6px;line-height:1}
.title-mark{width:14px;height:14px;border-radius:50%;background:var(--red);margin-bottom:24px}
.section-title.light{color:var(--white)}

/* About */
.about-title{position:absolute;left:138px;top:812px}
.about-lead{position:absolute;left:150px;top:878px;width:490px;font-size:17px;line-height:26px;color:var(--ink)}
.about-body{position:absolute;left:150px;top:970px;width:490px;font-size:15px;line-height:27px;color:var(--muted)}
.btn-red{position:absolute;height:46px;background:var(--red);color:var(--white);font-family:"Lato",sans-serif;font-size:15px;font-weight:400;display:flex;align-items:center;justify-content:center;text-transform:uppercase}
.about-btn{left:148px;top:1077px;width:162px}
.about-visual{position:absolute;left:690px;top:800px;width:400px;height:270px;border-radius:10px;background:linear-gradient(135deg,#f4f4f4,#d8d8d8)}
.about-visual-base{position:absolute;left:644px;top:1070px;width:490px;height:14px;border-radius:0 0 20px 20px;background:linear-gradient(#e6e6e6,#bdbdbd)}

/* Pricing */
.pricing-title{position:absolute;left:490px;top:1296px}
.price-card{position:absolute;top:1409px;height:401px;background:var(--white);box-shadow:0 2px 8px rgba(0,0,0,.18);text-align:center}
.price-head{height:87px;background:var(--card-head);font-family:"Lato",sans-serif;font-weight:700;font-size:28px;color:var(--ink);display:flex;align-items:center;justify-content:center}
.per-word{font-family:"Lato",sans-serif;font-size:24px;color:var(--red);margin-top:10px;line-height:28px}
.price-list{list-style:none;font-size:13.5px;line-height:26px;color:var(--text);margin-top:4px}
.card-basic{left:132px;width:289px}
.card-standard{left:451px;width:300px;background:var(--red)}
.card-standard .price-head{background:var(--dark);color:var(--white)}
.card-standard .per-word,.card-standard .price-list{color:var(--white)}
.card-standard .price-list{font-weight:600}
.card-premium{left:777px;width:292px}

/* Process */
.process-photo{position:absolute;left:0;top:1842px;width:590px;height:568px;
  background:linear-gradient(120deg,#efefef 0%,#e3dcd4 45%,#cdb9a2 80%,#b59a7c 100%)}
.process-title{position:absolute;left:582px;top:1968px}
.process-text{position:absolute;left:600px;top:2022px;width:482px;font-size:15px;line-height:25px;color:var(--muted)}
.check-list{position:absolute;left:600px;top:2120px;list-style:none;font-size:15px;line-height:32px;color:var(--ink)}
.check-list li{display:flex;align-items:center;gap:14px}
.check-list svg{width:10px;height:14px}
.process-btn{left:593px;top:2308px;width:150px;height:44px}

/* Testimonial */
.testimonial{position:absolute;left:0;top:2410px;width:1200px;height:465px;
  background:linear-gradient(100deg,#3a3a3a 0%,#4a4845 45%,#5b5650 70%,#3d3b39 100%)}
.testimonial-shade{position:absolute;inset:0;background:rgba(20,20,20,.35)}
.testimonial-title{position:absolute;left:405px;top:92px}
.avatar{position:absolute;left:234px;top:173px;width:160px;height:160px;border-radius:50%;border:4px solid var(--white);background:linear-gradient(160deg,#d9d3cf,#a99f99)}
.quote-mark{position:absolute;font-family:Georgia,serif;font-size:60px;color:var(--white);line-height:1}
.quote-text{position:absolute;left:430px;top:186px;width:520px;font-style:italic;font-size:17px;line-height:27px;color:var(--white)}
.quote-author{position:absolute;left:434px;top:284px;font-size:15px;font-weight:600;color:var(--white)}
.arrow{position:absolute;top:218px}

/* Footer */
.footer-nav{position:absolute;left:142px;top:2930px;display:flex;gap:28px;font-family:"Lato",sans-serif;font-weight:700;font-size:18px;color:var(--ink)}
.copyright{position:absolute;left:142px;top:2972px;font-size:13px;color:var(--text)}
.social{position:absolute;left:944px;top:2937px;display:flex;gap:8px}
.social span{width:34px;height:34px;border-radius:50%;border:2px solid var(--red)}
</style>
</head>
<body>

<header class="site-header">
  <div class="brand"><span>Velvet Orchard</span><span class="brand-dot"></span></div>
  <nav class="main-nav">
    <span class="active">Home</span><span>About Us</span><span>Pricing</span><span>Services</span><span>Process</span><span>Contact Us</span>
  </nav>
</header>

<section class="hero" role="img" aria-label="Woman reading a book beside a laptop in a cosy room">
  <div class="hero-shade"></div>
  <h1 class="hero-title">Need help publishing<br>a bestseller?</h1>
  <div class="btn-outline">Learn More</div>
  <div class="hero-dots"><span></span><span></span><span></span><span></span></div>
</section>
<svg class="abs" style="left:0;top:655px" width="1200" height="70" viewBox="0 0 1200 70">
  <polygon points="0,9 470,25 0,57" fill="#d4101e"/>
  <polygon points="0,57 470,25 1200,45 1200,70 0,70" fill="#ffffff"/>
</svg>

<section class="about">
  <h2 class="section-title about-title"><span class="title-mark"></span>About Velvet Orchard</h2>
  <p class="about-lead">Our proofreading, editing and manuscript review packages are specifically tailored to help you publish the best possible version of your story.</p>
  <p class="about-body">enim In massa libero interdum nec interdum vel blandit sed nulla In ullamcorper est eget tempor cursus neque mi consectetuer mi a ultricies massa est sed nisl Class aptent taciti sociosqu</p>
  <div class="btn-red about-btn">Read More</div>
  <div class="about-visual" role="img" aria-label="Laptop showing a manuscript page with red proofreading marks"></div>
  <div class="about-visual-base"></div>
</section>

<svg class="abs" style="left:0;top:1195px" width="1200" height="650" viewBox="0 0 1200 650">
  <polygon points="0,11 1200,40 1200,647 0,647" fill="#ebebeb"/>
  <polygon points="730,35 1200,0 1200,50" fill="#1f1f1f"/>
  <polygon points="900,45 1200,25 1200,80" fill="#2d2d2d"/>
</svg>

<section class="pricing">
  <h2 class="section-title pricing-title"><span class="title-mark"></span>Our Pricing</h2>
  <div class="price-card card-basic">
    <div class="price-head">$.02</div>
    <div class="per-word">PER WORD</div>
    <ul class="price-list"><li>Proofreading</li><li>Line Edit (Copy-editing)</li><li>Fix spelling and grammar</li><li>Sales copy/summary revision</li></ul>
  </div>
  <div class="price-card card-standard">
    <div class="price-head">$.04</div>
    <div class="per-word">PER WORD</div>
    <ul class="price-list"><li>Proofreading</li><li>Line Edit (Copy-editing)</li><li>Fix spelling and grammar</li><li>Sales copy/summary revision</li><li>Organization and content</li><li>Plot and pacing</li><li>Manuscript Review</li></ul>
  </div>
  <div class="price-card card-premium">
    <div class="price-head">$.06</div>
    <div class="per-word">PER WORD</div>
    <ul class="price-list"><li>Proofreading</li><li>Line Edit (Copy-editing)</li><li>Fix spelling and grammar</li><li>Sales copy/summary revision</li><li>Organization and content</li><li>Plot and pacing</li><li>Manuscript Review</li><li>Formatting (print and ebook)</li><li>Pre-publication proofread</li></ul>
  </div>
</section>

<section class="process">
  <div class="process-photo" role="img" aria-label="Smiling woman at a desk with books and a laptop"></div>
  <svg class="abs" style="left:0;top:1840px" width="1200" height="90" viewBox="0 0 1200 90">
    <polygon points="0,2 1200,2 1200,85 590,40 590,2" fill="#ebebeb"/>
    <polygon points="0,2 140,35 0,42" fill="#d4101e"/>
    <polygon points="140,35 590,40 590,2 0,2" fill="#ebebeb"/>
  </svg>
  <h2 class="section-title process-title"><span class="title-mark"></span>Our Process</h2>
  <p class="process-text">Send us a sample of your book. Our caffeine-fueled, eagle-eyed editors will go through it and then email you with their comments and suggestions. You can ask them any questions you want. They will look for…</p>
  <ul class="check-list">
    <li><svg viewBox="0 0 10 14"><polyline points="2,2 8,7 2,12" fill="none" stroke="#d4101e" stroke-width="3"/></svg>Typos and grammatical errors.</li>
    <li><svg viewBox="0 0 10 14"><polyline points="2,2 8,7 2,12" fill="none" stroke="#d4101e" stroke-width="3"/></svg>Spelling and word choice issues</li>
    <li><svg viewBox="0 0 10 14"><polyline points="2,2 8,7 2,12" fill="none" stroke="#d4101e" stroke-width="3"/></svg>Punctuation and style</li>
    <li><svg viewBox="0 0 10 14"><polyline points="2,2 8,7 2,12" fill="none" stroke="#d4101e" stroke-width="3"/></svg>Word choice, clarity and flow.</li>
    <li><svg viewBox="0 0 10 14"><polyline points="2,2 8,7 2,12" fill="none" stroke="#d4101e" stroke-width="3"/></svg>Sentence structure and craft</li>
  </ul>
  <div class="btn-red process-btn">Read More</div>
</section>

<section class="testimonial" role="img" aria-label="Man writing at a desk in a dim bookshop">
  <div class="testimonial-shade"></div>
  <h2 class="section-title light testimonial-title"><span class="title-mark" style="background:#ffffff"></span>What Our Book Seller Says</h2>
  <svg class="arrow" style="left:150px" width="24" height="44" viewBox="0 0 24 44"><polyline points="22,2 2,22 22,42" fill="none" stroke="#ffffff" stroke-width="2"/></svg>
  <div class="avatar" role="img" aria-label="Portrait of a reviewing author"></div>
  <span class="quote-mark" style="left:404px;top:158px">“</span>
  <p class="quote-text">Ai quis lacus mollis aliquam Curabitur iaculis tempus eros Curabitur vel mi sit amet magna malesuada ultrices Ut nisi erat fermentum vel congue id euismod in elit Fusce ultri</p>
  <span class="quote-mark" style="left:850px;top:240px">”</span>
  <p class="quote-author">By Author Name</p>
  <svg class="arrow" style="left:1026px" width="24" height="44" viewBox="0 0 24 44"><polyline points="2,2 22,22 2,42" fill="none" stroke="#ffffff" stroke-width="2"/></svg>
</section>
<svg class="abs" style="left:0;top:2375px" width="1200" height="60" viewBox="0 0 1200 60">
  <polygon points="0,36 870,36 1200,0 1200,36" fill="#d4101e" opacity="0"/>
  <polygon points="870,35 1200,5 1200,45" fill="#d4101e"/>
</svg>
<svg class="abs" style="left:0;top:2850px" width="1200" height="30" viewBox="0 0 1200 30">
  <polygon points="0,25 1200,0 1200,30 0,30" fill="#ffffff"/>
  <polygon points="0,0 240,18 0,25" fill="#ffffff"/>
</svg>

<footer>
  <nav class="footer-nav"><span>Home</span><span>About Us</span><span>Pricing</span><span>Services</span><span>Process</span><span>Contact Us</span></nav>
  <p class="copyright">© 2018 Company Name All right reserved</p>
  <div class="social" aria-label="Social links"><span></span><span></span><span></span></div>
</footer>

</body>
</html>
```